I need a business card to give to prospective clients. I am a freelance photographer who photographs most things (except weddings and social stuff) including nature, wildlife and interiors.
I want to look modern and stylish.
I am including a photograph although I am by no means certain that it should be used - what do you think?
More of my images can be seen and downloaded at my PixelVault page - just search for Marnie Fulbright
Target Market(s)
Home owners selling or letting properties, private individuals wanting to buy prints
Industry/Entity Type
Business
Contact Information for Business Card
Marnie Fulbright Photography
Marnie
Tarlow Cottage, Brindle Orchard Way, Wexcombe Parva, Bury St Edmunds, IP31 4QX
Tel: +44 7700 314862. Email: marnie@marniefulbright-example.co.uk

```html
<!DOCTYPE html>
<html lang="en">
<head>
<meta charset="utf-8">
<title>Marnie Fulbright Photography – Business Card</title>
<link rel="stylesheet" href="https://fonts.googleapis.com/css2?family=Libre+Bodoni:wght@400;700&family=Libre+Baskerville&family=Questrial&display=swap">
<style>
  :root {
    --ink: #111111;
    --paper: #ffffff;
    --table: #e8e2db;
    --cocoa-deep: #24160d;
    --cocoa: #3b271a;
    --cocoa-light: #57402e;
    --bronze: #c27a34;
    --cream: #f4eee6;
    --photo-warm: #b89a74;
    --photo-shade: #5e4733;
  }
  * { box-sizing: border-box; margin: 0; padding: 0; }
  html, body { width: 1200px; height: 1000px; overflow: hidden; }
  body { background: var(--table); font-family: "Libre Baskerville", serif; }

  .brand-header {
    height: 250px; background: var(--paper);
    display: flex; flex-direction: column; align-items: center; padding-top: 22px;
  }
  .brand-header .mark-circle {
    width: 120px; height: 120px; border-radius: 50%; border: 3px solid var(--ink);
  }
  .wordmark-name {
    font-family: "Libre Bodoni", serif; font-weight: 700; text-transform: uppercase; line-height: 1.1;
  }
  .wordmark-tag {
    font-family: "Questrial", sans-serif; font-weight: 400; text-transform: lowercase; line-height: 1.1;
  }
  .brand-header .wordmark-name { margin-top: 30px; font-size: 36px; color: var(--ink); }
  .brand-header .wordmark-tag { font-size: 17px; color: var(--ink); letter-spacing: 6px; }

  .card-stage {
    height: 750px; display: flex; align-items: center; justify-content: center; gap: 40px;
  }
  .card {
    position: relative; width: 540px; height: 310px; overflow: hidden;
    background: linear-gradient(100deg, var(--cocoa-deep) 0%, var(--cocoa) 60%, var(--cocoa-light) 100%);
    box-shadow: 0 14px 30px rgba(40, 25, 15, 0.35);
  }

  /* Back of card */
  .card-back .photo-area {
    position: absolute; inset: 0;
    background: linear-gradient(160deg, var(--photo-warm) 0%, #8a6c4d 45%, var(--photo-shade) 100%);
    clip-path: polygon(34% 0, 100% 0, 100% 100%, 56% 100%);
    opacity: 0.9;
  }
  .card-back .photo-veil {
    position: absolute; inset: 0;
    background: rgba(36, 22, 13, 0.35);
    clip-path: polygon(34% 0, 62% 0, 56% 100%, 46% 100%);
  }
  .card-back .identity { position: absolute; left: 34px; top: 26px; }
  .card-back .mark-circle {
    width: 46px; height: 46px; border-radius: 50%; border: 2px solid var(--bronze); margin-left: 60px;
  }
  .card-back .wordmark-name { margin-top: 10px; font-size: 20px; color: var(--bronze); }
  .card-back .wordmark-tag { font-size: 11px; color: var(--bronze); letter-spacing: 5px; }
  .card-back .address {
    position: absolute; left: 34px; top: 160px; color: var(--cream);
    font-size: 12.5px; line-height: 1.3; font-style: normal;
  }
  .card-back .phone { margin-top: 14px; }
  .card-back .email { font-family: "Questrial", sans-serif; font-size: 11px; margin-top: 4px; }

  /* Front of card */
  .card-front { display: flex; flex-direction: column; align-items: center; justify-content: center; }
  .card-front .mark-circle {
    width: 100px; height: 100px; border-radius: 50%; border: 3px solid var(--bronze);
  }
  .card-front .wordmark-name { margin-top: 18px; font-size: 30px; color: var(--bronze); }
  .card-front .wordmark-tag { font-size: 15px; color: var(--bronze); letter-spacing: 6px; }
</style>
</head>
<body>
  <header class="brand-header">
    <div class="mark-circle"></div>
    <div class="wordmark-name">Marnie Fulbright</div>
    <div class="wordmark-tag">photography</div>
  </header>

  <main class="card-stage">
    <section class="card card-back">
      <div class="photo-area" role="img" aria-label="Interior photograph of a bright dining room with wicker chairs around a table beside a window"></div>
      <div class="photo-veil"></div>
      <div class="identity">
        <div class="mark-circle"></div>
        <div class="wordmark-name">Marnie Fulbright</div>
        <div class="wordmark-tag">photography</div>
      </div>
      <address class="address">
        <div>Tarlow Cottage</div>
        <div>Brindle Orchard Way</div>
        <div>Wexcombe Parva</div>
        <div>Kelsborough, IP31 4QX</div>
        <div class="phone">Tel: +44 7700 314862</div>
        <div class="email">Email: marnie@marniefulbright-example.co.uk</div>
      </address>
    </section>

    <section class="card card-front">
      <div class="mark-circle"></div>
      <div class="wordmark-name">Marnie Fulbright</div>
      <div class="wordmark-tag">photography</div>
    </section>
  </main>
</body>
</html>
```